colour pencil case design

I am looking for a design for the front of a pencil case. The pencil case has 2 versions, 1 white fabric and 1 black fabric. The design should have 2 versions, eg. white word on black fabric and black words on white fabric. Its for children and teenagers’ aged 7 to 18. I can have 2 separate designs.
The pencil case is 22cm by 14cm. So the size of the image should be 18cm by 11cm. Files should be in png format and already in the correct size.
It must have the word “Believe”in big size. The letter b can be in capps or small letter. Prefer the font used in
I am looking for a background or image that can represent the phrase. If the design is good, I am open to also black and white theme.
Can also be black and white or colour... I have attached the font that I like for the main word "Believe". https://www.quintarro.net/gallery/583019447/Free-Font-Norvelle-Modern-Script. Or you can use this font for the word Believe as well…. "Playlist script
Besides the word Believe, you should have the sentence ‘you can and you will”. It can be all in capps or small letter. (smaller size and different font from your word.
Target Market(s)
children and teenagers
Industry/Entity Type
tuition
Requirements
Must have
- The word Believe and the phrase I can and I will
Nice to have
- Some colourful pictures that can represent the phrase

```html
<!DOCTYPE html>
<html lang="en">
<head>
<meta charset="utf-8">
<title>Believe – Pencil Case Front, Light and Dark Versions</title>
<link rel="stylesheet" href="https://fonts.googleapis.com/css2?family=Yellowtail&family=Jost:wght@300;400&display=swap">
<style>
  :root {
    --page: #ffffff;
    --light-fabric-top: #f4f4f4;
    --light-fabric-bottom: #d9d8d7;
    --light-scene: #bdbbb9;
    --dark-fabric-top: #3a3a3a;
    --dark-fabric-bottom: #2b2b2b;
    --dark-scene: #4a4a4a;
    --ink-dark: #0d0d0d;
    --ink-light: #ffffff;
    --crayon-teal: #17b38f;
    --crayon-blue: #2f8fd6;
    --crayon-orange: #f26a1b;
    --crayon-brown: #a48224;
    --crayon-green: #2fb84a;
  }
  * { box-sizing: border-box; margin: 0; padding: 0; }
  html, body {
    width: 997px;
    height: 1200px;
    overflow: hidden;
    background: var(--page);
  }
  .canvas {
    position: relative;
    width: 997px;
    height: 1200px;
  }
  .case-front {
    position: absolute;
    left: 62px;
    width: 877px;
    height: 537px;
    overflow: hidden;
    box-shadow: 0 3px 6px rgba(0, 0, 0, 0.25);
  }
  .case-front--light { top: 42px; }
  .case-front--dark { top: 608px; }

  .scene {
    position: absolute;
    inset: 0;
  }
  .case-front--light .scene {
    background:
      radial-gradient(ellipse 45% 55% at 72% 52%, var(--light-scene) 0%, transparent 70%),
      radial-gradient(ellipse 25% 60% at 8% 70%, var(--light-scene) 0%, transparent 75%),
      linear-gradient(180deg, var(--light-fabric-top), var(--light-fabric-bottom));
  }
  .case-front--dark .scene {
    background:
      radial-gradient(ellipse 45% 55% at 72% 52%, var(--dark-scene) 0%, transparent 70%),
      radial-gradient(ellipse 25% 60% at 8% 70%, var(--dark-scene) 0%, transparent 75%),
      linear-gradient(180deg, var(--dark-fabric-top), var(--dark-fabric-bottom));
  }

  .crayon {
    position: absolute;
    border-radius: 40% 40% 45% 45% / 6% 6% 8% 8%;
    opacity: 0.95;
  }
  .crayon--teal   { left: 0;     top: 114px; width: 19px; height: 384px; background: var(--crayon-teal); }
  .crayon--blue-a { left: 43px;  top: 0;     width: 14px; height: 216px; background: var(--crayon-blue); }
  .crayon--blue-b { left: 82px;  top: 0;     width: 36px; height: 474px; background: var(--crayon-blue); }
  .crayon--orange { left: 766px; top: 216px; width: 36px; height: 282px; background: var(--crayon-orange); }
  .crayon--brown  { left: 818px; top: 96px;  width: 18px; height: 276px; background: var(--crayon-brown); }
  .crayon--green  { left: 854px; top: 270px; width: 23px; height: 228px; background: var(--crayon-green); }

  .headline {
    position: absolute;
    left: 100px;
    top: 70px;
    width: 700px;
    text-align: center;
    font-family: "Yellowtail", cursive;
    font-weight: 400;
    font-size: 250px;
    line-height: 1;
    transform: rotate(-3deg);
  }
  .tagline {
    position: absolute;
    left: 0;
    top: 404px;
    width: 810px;
    text-align: center;
    font-family: "Jost", sans-serif;
    font-weight: 300;
    font-size: 25px;
    letter-spacing: 0.5px;
    text-transform: uppercase;
  }
  .case-front--light .headline,
  .case-front--light .tagline { color: var(--ink-dark); }
  .case-front--dark .headline,
  .case-front--dark .tagline { color: var(--ink-light); }
</style>
</head>
<body>
  <main class="canvas">
    <section class="case-front case-front--light" aria-label="Design for white fabric">
      <div class="scene" role="img" aria-label="Soft grey illustration of a lakeside cottage among pine trees"></div>
      <span class="crayon crayon--teal"></span>
      <span class="crayon crayon--blue-a"></span>
      <span class="crayon crayon--blue-b"></span>
      <span class="crayon crayon--orange"></span>
      <span class="crayon crayon--brown"></span>
      <span class="crayon crayon--green"></span>
      <h1 class="headline">Believe</h1>
      <p class="tagline">You can and you will</p>
    </section>

    <section class="case-front case-front--dark" aria-label="Design for black fabric">
      <div class="scene" role="img" aria-label="Dark grey illustration of a lakeside cottage among pine trees"></div>
      <span class="crayon crayon--teal"></span>
      <span class="crayon crayon--blue-a"></span>
      <span class="crayon crayon--blue-b"></span>
      <span class="crayon crayon--orange"></span>
      <span class="crayon crayon--brown"></span>
      <span class="crayon crayon--green"></span>
      <h2 class="headline">Believe</h2>
      <p class="tagline">You can and you will</p>
    </section>
  </main>
</body>
</html>
```